Brochure Design Project

11x17 flat...folds to 8.5x11
full color
Utilize customers images and web content to create sleek brochure showcasing customers capabilities.
www.plumfeatherworks.com
Logo added to uploads.
Reason: Customer is out of town.

```html
<!DOCTYPE html>
<html lang="en">
<head>
<meta charset="utf-8">
<title>Creating Memorable Events – Brochure Panel</title>
<link rel="stylesheet" href="https://fonts.googleapis.com/css2?family=Jost:wght@700&family=Didact+Gothic&family=Montserrat:wght@700&display=swap">
<style>
  :root {
    --green-glow: #78cc2e;
    --green-mid: #4fa51c;
    --green-dark: #2a780c;
    --lime: #8fe01e;
    --frame-black: #111111;
    --frame-white: #ffffff;
    --heading: #d4f21a;
    --body: #f2f26a;
    --ribbon: #d8262b;
    --ribbon-dark: #9c1418;
    --ribbon-text: #ffffff;
  }
  * { margin: 0; padding: 0; box-sizing: border-box; }
  html, body { width: 1200px; height: 776px; overflow: hidden; }
  .panel {
    position: relative;
    width: 1200px;
    height: 776px;
    overflow: hidden;
    background: radial-gradient(ellipse 70% 75% at 62% 45%, var(--green-glow) 0%, var(--green-mid) 55%, var(--green-dark) 100%);
  }
  .showcase { position: absolute; left: 0; top: 0; width: 600px; height: 700px; }
  .ribbon { position: absolute; left: 630px; top: 22px; width: 540px; height: 110px; }
  .ribbon-label {
    font-family: "Montserrat", sans-serif;
    font-weight: 700;
    font-size: 21px;
    letter-spacing: 0.5px;
    fill: var(--ribbon-text);
  }
  .services {
    position: absolute;
    left: 610px;
    top: 155px;
    width: 590px;
    text-align: center;
  }
  .services-title {
    font-family: "Jost", sans-serif;
    font-weight: 700;
    font-size: 38px;
    line-height: 54px;
    letter-spacing: 0;
    color: var(--heading);
    text-shadow: 2px 2px 3px rgba(0, 50, 0, 0.45);
    margin-left: -42px;
  }
  .services-copy {
    font-family: "Didact Gothic", sans-serif;
    font-size: 34px;
    line-height: 42px;
    color: var(--body);
    margin-top: 40px;
    text-shadow: 1px 1px 2px rgba(0, 50, 0, 0.3);
    white-space: nowrap;
  }
  .services-copy + .services-copy { margin-top: 46px; }
</style>
</head>
<body>
<main class="panel">
  <svg class="showcase" viewBox="0 0 600 700">
    <defs>
      <linearGradient id="collage-tones" x1="0" y1="0" x2="1" y2="1">
        <stop offset="0" stop-color="#e0a13a"/>
        <stop offset="0.3" stop-color="#4c78b8"/>
        <stop offset="0.55" stop-color="#c8c2bc"/>
        <stop offset="0.8" stop-color="#b4503e"/>
        <stop offset="1" stop-color="#6b4f7c"/>
      </linearGradient>
    </defs>
    <polygon class="frame-lime" fill="var(--lime)" points="24,456 96,178 382,98 586,282 576,566 226,660"/>
    <polygon class="frame-black" fill="var(--frame-black)" points="46,454 112,192 380,116 568,290 558,550 232,640"/>
    <polygon class="frame-white" fill="var(--frame-white)" points="60,452 122,202 378,128 556,296 546,540 236,626"/>
    <polygon class="project-collage" fill="url(#collage-tones)" role="img"
      aria-label="Collage of past event and print projects: photo booth flyers, personalised mugs and keychains, green-screen photos, caricature samples and portrait keepsakes"
      points="74,448 134,212 376,140 544,302 534,530 240,612"/>
  </svg>

  <svg class="ribbon" viewBox="0 0 540 110">
    <path class="ribbon-tail" fill="var(--ribbon-dark)" d="M6,30 L70,30 L70,84 L6,84 L28,57 Z"/>
    <path class="ribbon-tail" fill="var(--ribbon-dark)" d="M534,18 L470,18 L470,72 L534,72 L512,45 Z"/>
    <path class="ribbon-band" fill="var(--ribbon)" d="M40,28 Q270,4 500,18 L500,74 Q270,60 40,84 Z"/>
    <path id="ribbon-arc" fill="none" d="M70,70 Q270,40 470,60"/>
    <text class="ribbon-label" text-anchor="middle">
      <textPath href="#ribbon-arc" startOffset="50%">CREATING MEMORABLE EVENTS</textPath>
    </text>
  </svg>

  <section class="services">
    <h1 class="services-title">DESIGN&nbsp; PRODUCTION<br>INTERACTIVE ACTIVITIES</h1>
    <p class="services-copy">We have over 36 years of<br>experience in Interactive Activities<br>and Design Production.</p>
    <p class="services-copy">Our unparalleled services<br>have been requested both<br>locally and nationally.</p>
  </section>
</main>
</body>
</html>
```